Silver Creek Plumbing Business card & letter head design

We need a new business card and letter head for our plumbing company called silver creek plumbing. attached is the companys logo. We provide domestic and commercial plumbing services in regional western Australia. We are after Something simple yet nice to look at and something that fits within the trade industry.

Target Market(s)

trade/building industry

Contact Information for Business Card

Darl Hensby
Manager
0461 238 574
enquiries@scplumbwork.net.au
ABN: 47 381 905 462
PCL: 5187

Domestic & Commercial Plumbing
Tip Truck & Excavator hire

Colors

Designer to choose colors to be used in the design.

```html
<!DOCTYPE html>
<html lang="en">
<head>
<meta charset="utf-8">
<title>Silver Creek Plumbing – Stationery</title>
<link rel="stylesheet" href="https://fonts.googleapis.com/css2?family=Lato:wght@400;700;900&family=Montserrat:wght@700;800&display=swap">
<style>
  :root {
    --brand-blue: #0c58a8;
    --brand-grey: #58595b;
    --ink: #6d6e71;
    --paper: #ffffff;
    --backdrop: #e4e4e4;
  }
  * { box-sizing: border-box; margin: 0; padding: 0; }
  html, body { width: 1200px; height: 971px; overflow: hidden; }
  body {
    background: var(--backdrop);
    font-family: "Lato", sans-serif;
    color: var(--ink);
    position: relative;
  }

  /* Letterhead */
  .letterhead {
    position: absolute; left: 70px; top: 70px;
    width: 580px; height: 820px;
    background: var(--paper);
    box-shadow: 0 4px 18px rgba(0,0,0,.12);
    overflow: hidden;
  }
  .brand-name {
    display: flex; align-items: center; gap: 7px;
    font-family: "Montserrat", sans-serif; font-weight: 800;
    color: var(--brand-blue); text-transform: uppercase; letter-spacing: .02em;
    line-height: 1.05;
  }
  .brand-name .dot { width: 10px; height: 10px; border-radius: 50%; background: currentColor; flex: none; }
  .letterhead .brand-name { position: absolute; left: 44px; top: 60px; font-size: 17px; width: 150px; }
  .contact-list { list-style: none; font-size: 9.5px; line-height: 1.4; }
  .contact-list li { display: flex; align-items: flex-start; gap: 6px; }
  .contact-list svg { width: 9px; height: 9px; margin-top: 2px; flex: none; fill: var(--brand-blue); }
  .contact-list .reg { color: var(--brand-blue); font-weight: 700; padding-left: 15px; }
  .letterhead .contact-list { position: absolute; right: 44px; top: 52px; width: 190px; }

  .letter-body { position: absolute; left: 60px; top: 210px; width: 460px; font-size: 11px; line-height: 1.55; }
  .letter-body .date { margin-bottom: 14px; }
  .letter-body .recipient { margin-bottom: 30px; }
  .letter-body .salutation { margin-bottom: 24px; }
  .letter-body p.para { margin-bottom: 18px; }
  .letter-body .closing { margin-top: 12px; margin-bottom: 18px; }
  .signatory { font-family: "Montserrat", sans-serif; font-weight: 800; font-size: 14px; color: var(--brand-grey); }
  .role { font-size: 10px; }
  .signature { width: 170px; height: 46px; margin-top: 10px; background: linear-gradient(90deg, rgba(12,88,168,.12), rgba(12,88,168,.04)); }

  .footer-wave { position: absolute; left: 0; bottom: 0; width: 100%; display: block; }

  /* Business cards */
  .card {
    position: absolute; left: 720px; width: 420px; height: 240px;
    box-shadow: 0 4px 14px rgba(0,0,0,.14);
    overflow: hidden;
  }
  .card-back { top: 170px; background: var(--brand-blue); display: flex; align-items: center; justify-content: center; }
  .card-back .brand-name { color: var(--paper); font-size: 24px; width: 210px; }
  .card-front { top: 470px; background: var(--paper); }
  .card-front .brand-name { position: absolute; left: 34px; top: 68px; font-size: 17px; width: 150px; }
  .card-front .holder { position: absolute; left: 232px; top: 28px; }
  .card-front .holder .signatory { color: var(--brand-blue); font-size: 13px; }
  .card-front .holder .role { font-size: 8.5px; margin-bottom: 8px; }
  .card-front .contact-list { font-size: 8.5px; }
</style>
</head>
<body>

<section class="letterhead">
  <div class="brand-name"><span class="dot"></span><span>Silver Creek Plumbing</span></div>

  <ul class="contact-list">
    <li><svg viewBox="0 0 10 10"><path d="M2 0.5 L4 2.5 L3 3.8 Q4.5 6 6.2 7 L7.5 6 L9.5 8 L8 9.5 Q2 8.5 0.5 2 Z"/></svg>0461 238 574</li>
    <li><svg viewBox="0 0 10 10"><path d="M0 4 L10 0 L6 10 L5 5.5 Z"/></svg>enquiries@scplumbwork.net.au</li>
    <li><svg viewBox="0 0 10 10"><circle cx="5" cy="5" r="4" fill="none" stroke="#0c58a8" stroke-width="1.5"/></svg>www.scplumbwork.net.au</li>
    <li><svg viewBox="0 0 10 10"><path d="M5 0 A3.5 3.5 0 0 1 8.5 3.5 Q8.5 6 5 10 Q1.5 6 1.5 3.5 A3.5 3.5 0 0 1 5 0 Z"/></svg>27 Harlow Crest Rd.<br>Marlowe, WA 6432</li>
    <li class="reg">ABN: 47 381 905 462</li>
    <li class="reg">PCL: 5187</li>
  </ul>

  <div class="letter-body">
    <div class="date">03.12.2019</div>
    <div class="recipient">Recipient name<br>54 Kestrel Way<br>Brindle Bay, WA 6510</div>
    <div class="salutation">Dear, Mr ____________</div>
    <p class="para">Lorem Ipsum is simply dummy text of the printing and typesetting industry. Lorem Ipsum has been the industry's standard dummy text ever since the 1500s, when an unknown printer took a galley of type and scrambled it to make a type specimen book. It has survived not only five centuries, but also the leap into electronic typesetting, remaining essentially unchanged.</p>
    <p class="para">Lorem Ipsum is simply dummy text of the printing and typesetting industry. Lorem Ipsum has been the industry's standard dummy text ever since the 1500s.</p>
    <p class="para">Lorem Ipsum is simply dummy text of the printing and typesetting industry.</p>
    <div class="closing">Kind Regards</div>
    <div class="signatory">Darl Hensby</div>
    <div class="role">Manager</div>
    <div class="signature" role="img" aria-label="Handwritten signature of Darl Hensby"></div>
  </div>

  <svg class="footer-wave" viewBox="0 0 580 210" aria-hidden="false">
    <path d="M330 118 C440 100 530 60 580 8 L580 20 C520 75 440 108 330 118 Z" fill="var(--brand-grey)"/>
    <path d="M0 210 L0 170 C140 95 380 110 580 35 L580 210 Z" fill="var(--brand-blue)"/>
    <rect x="0" y="190" width="580" height="20" fill="var(--brand-grey)"/>
    <text x="560" y="180" text-anchor="end" font-family="Lato, sans-serif" font-size="11" fill="#ffffff">Domestic &amp; Commercial Plumbing &#160;|&#160; Tip Truck &amp; Excavator hire</text>
  </svg>
</section>

<section class="card card-back">
  <div class="brand-name"><span class="dot"></span><span>Silver Creek Plumbing</span></div>
</section>

<section class="card card-front">
  <div class="brand-name"><span class="dot"></span><span>Silver Creek Plumbing</span></div>
  <div class="holder">
    <div class="signatory">Darl Hensby</div>
    <div class="role">Manager</div>
    <ul class="contact-list">
      <li><svg viewBox="0 0 10 10"><path d="M2 0.5 L4 2.5 L3 3.8 Q4.5 6 6.2 7 L7.5 6 L9.5 8 L8 9.5 Q2 8.5 0.5 2 Z"/></svg>0461 238 574</li>
      <li><svg viewBox="0 0 10 10"><path d="M0 4 L10 0 L6 10 L5 5.5 Z"/></svg>enquiries@scplumbwork.net.au</li>
      <li><svg viewBox="0 0 10 10"><circle cx="5" cy="5" r="4" fill="none" stroke="#0c58a8" stroke-width="1.5"/></svg>www.scplumbwork.net.au</li>
      <li><svg viewBox="0 0 10 10"><path d="M5 0 A3.5 3.5 0 0 1 8.5 3.5 Q8.5 6 5 10 Q1.5 6 1.5 3.5 A3.5 3.5 0 0 1 5 0 Z"/></svg>27 Harlow Crest Rd.<br>Marlowe, WA 6432</li>
      <li class="reg">ABN: 47 381 905 462</li>
      <li class="reg">PCL: 5187</li>
    </ul>
  </div>
  <svg class="footer-wave" viewBox="0 0 420 90">
    <path d="M200 40 C300 32 380 15 420 0 L420 9 C370 28 300 38 200 40 Z" fill="var(--brand-grey)"/>
    <path d="M0 90 L0 70 C110 30 280 45 420 12 L420 90 Z" fill="var(--brand-blue)"/>
    <rect x="0" y="80" width="420" height="10" fill="var(--brand-grey)"/>
    <text x="405" y="74" text-anchor="end" font-family="Lato, sans-serif" font-size="8.5" fill="#ffffff">Domestic &amp; Commercial Plumbing &#160;|&#160; Tip Truck &amp; Excavator hire</text>
  </svg>
</section>

</body>
</html>
```